Hallo,
ich bin gerade dabei, ein ebook über alternative Heilmethoden für die Frauenkrankheit Endometriose zu schreiben. Dafür brauche ich ein ausdrucksstarkes Cover. Meine Zielgruppe sind dementsprechend Frauen, die Endometriose haben. Bei Endometriose wächst Schleimhaut aus der Gebärmutter im Bauchraum, den Eierstöcken usw. Symptome sind u.a. starke Schmerzen und Kinderlosigkeit. Die Krankheit ist schulmedizinisch nicht gut behandelbar und nicht heilbar, aber es gibt zahlreiche alternative Heilmethoden, die die Symptome lindern können. Darüber soll das Buch handeln. Hier die Website zum Buch: http://www.lindenblattwissen.de/
Vielen Dank und freundliche Grüße
Katrin Wollny
Das Cover soll eine positive Stimmung rüber bringen. So wie das Bild auf der Website. Leider darf ich das Bild nur für die Website verwenden.

```html
<!DOCTYPE html>
<html lang="de">
<head>
<meta charset="utf-8">
<title>Endometriose Wissen – Buchcover</title>
<link rel="stylesheet" href="https://fonts.googleapis.com/css2?family=Cabin+Condensed:wght@500;600&family=Share+Tech&display=swap">
<style>
  :root {
    --cream: #fdf8dc;
    --peach-deep: #f4b570;
    --peach-light: #fbe6cc;
    --brown: #5a3410;
    --orange: #e8890f;
    --sun-white: #fffaf0;
    --sun-gold: #f3a83e;
    --sun-amber: #d9741c;
    --coral: #e9876a;
    --sea: #b9854a;
  }
  html, body {
    margin: 0;
    padding: 0;
    overflow: hidden;
    background: var(--cream);
  }
  .cover {
    position: relative;
    width: 846px;
    height: 1200px;
    overflow: hidden;
    background: var(--cream);
  }
  .cover-art {
    position: absolute;
    inset: 0;
    width: 846px;
    height: 1200px;
  }
  .author {
    position: absolute;
    left: 28px;
    top: 22px;
    margin: 0;
    font-family: "Cabin Condensed", sans-serif;
    font-weight: 600;
    font-size: 37px;
    line-height: 1;
    color: var(--brown);
  }
  .title {
    position: absolute;
    left: 0;
    top: 900px;
    width: 846px;
    height: 110px;
    margin: 0;
  }
  .title text {
    font-family: "Share Tech", sans-serif;
  }
  .title .title-main { fill: var(--brown); }
  .title .title-accent { fill: var(--orange); }
  .subtitle {
    position: absolute;
    left: 0;
    top: 1044px;
    width: 846px;
    margin: 0;
    text-align: center;
    font-family: "Cabin Condensed", sans-serif;
    font-weight: 500;
    font-size: 39px;
    line-height: 48px;
    color: var(--orange);
  }
</style>
</head>
<body>
<main class="cover">
  <svg class="cover-art" viewBox="0 0 846 1200">
    <defs>
      <linearGradient id="sky" x1="0" y1="0" x2="1" y2="0.5">
        <stop offset="0" stop-color="#f4b370"/>
        <stop offset="0.5" stop-color="var(--peach-light)"/>
        <stop offset="1" stop-color="#fdf1e6"/>
      </linearGradient>
      <linearGradient id="photoBase" x1="0" y1="0" x2="0" y2="1">
        <stop offset="0" stop-color="#f8dcb8"/>
        <stop offset="0.45" stop-color="#f6c27a"/>
        <stop offset="0.8" stop-color="#eda03f"/>
        <stop offset="1" stop-color="var(--sea)"/>
      </linearGradient>
      <radialGradient id="sunGlow" cx="0.3" cy="0.62" r="0.42">
        <stop offset="0" stop-color="var(--sun-white)"/>
        <stop offset="0.4" stop-color="#fce9c4" stop-opacity="0.9"/>
        <stop offset="1" stop-color="#f8cf86" stop-opacity="0"/>
      </radialGradient>
      <radialGradient id="coralRight" cx="0.82" cy="0.6" r="0.35">
        <stop offset="0" stop-color="var(--coral)" stop-opacity="0.85"/>
        <stop offset="1" stop-color="var(--coral)" stop-opacity="0"/>
      </radialGradient>
      <radialGradient id="amberLeft" cx="0.1" cy="0.75" r="0.3">
        <stop offset="0" stop-color="var(--sun-amber)" stop-opacity="0.75"/>
        <stop offset="1" stop-color="var(--sun-amber)" stop-opacity="0"/>
      </radialGradient>
      <linearGradient id="fadeTop" x1="0" y1="0" x2="0" y2="1">
        <stop offset="0" stop-color="#fbe3c6" stop-opacity="1"/>
        <stop offset="0.3" stop-color="#fbe6cc" stop-opacity="0.75"/>
        <stop offset="0.55" stop-color="#fbe6cc" stop-opacity="0"/>
      </linearGradient>
    </defs>

    <rect class="sky-band" x="0" y="0" width="846" height="860" fill="url(#sky)"/>

    <g class="photo-area" role="img" aria-label="Foto: fröhliche junge Frauen springen bei Sonnenuntergang am Strand in die Luft – Lebensfreude trotz Endometriose">
      <path id="photoShape" d="M0 180 L846 180 L846 826 Q 560 880 420 852 Q 180 812 0 753 Z" fill="url(#photoBase)"/>
      <path d="M0 180 L846 180 L846 826 Q 560 880 420 852 Q 180 812 0 753 Z" fill="url(#amberLeft)"/>
      <path d="M0 180 L846 180 L846 826 Q 560 880 420 852 Q 180 812 0 753 Z" fill="url(#coralRight)"/>
      <path d="M0 180 L846 180 L846 826 Q 560 880 420 852 Q 180 812 0 753 Z" fill="url(#sunGlow)"/>
      <path d="M0 180 L846 180 L846 826 Q 560 880 420 852 Q 180 812 0 753 Z" fill="url(#fadeTop)"/>
    </g>

    <path class="arc-line" d="M0 99 Q 420 60 846 230" fill="none" stroke="#fdf3e6" stroke-width="1.5" opacity="0.9"/>
    <path class="photo-edge" d="M0 753 Q 180 812 420 852 Q 560 880 846 826" fill="none" stroke="var(--orange)" stroke-width="3"/>
  </svg>

  <p class="author">Katrin Wollny</p>

  <svg class="title" viewBox="0 900 846 110" role="heading" aria-level="1" aria-label="Endometriose Wissen">
    <text class="title-main" x="76" y="993" font-size="80" textLength="461" lengthAdjust="spacing">ENDOMETRIOSE</text>
    <text class="title-accent" x="548" y="993" font-size="102" textLength="223" lengthAdjust="spacing">WISSEN</text>
  </svg>

  <p class="subtitle">Alternative Behandlungsmethoden<br>zur Linderung der Beschwerden</p>
</main>
</body>
</html>
```